Business cards for landscaping company
Torvend Landscaping, LLC
Business cards for landscaping company - Construction
Creative Brief
Professional
Wesley R. Torvend
Owner
47 Birchell Lane Palmer, MA 01082
torvendlandscaping@quillmail.example
Landscape Design/ Excavation Paver Walkways/ Patios Hydroseeding New lawn installations Commercial Property Maintenance Custom Outdoor Living Areas Snow and Ice Management

```html
<!DOCTYPE html>
<html lang="en">
<head>
<meta charset="utf-8">
<title>Torvend Landscaping, LLC — Business Cards</title>
<link rel="stylesheet" href="https://fonts.googleapis.com/css2?family=Didact+Gothic&display=swap">
<style>
  :root {
    --bg: #2a2a2c;
    --card-black: #0b0b0c;
    --card-ink: #f2f2f2;
    --silver-light: #e6e8ea;
    --silver-mid: #b7bbbf;
    --silver-dark: #8d9296;
    --name-ink: #2b2d30;
    --tab-light: #d9d9d9;
    --tab-dark: #6f6f6f;
  }
  html, body {
    margin: 0;
    width: 1200px;
    height: 896px;
    overflow: hidden;
    background: var(--bg);
  }
  .stage {
    display: block;
    width: 1200px;
    height: 896px;
    font-family: "Didact Gothic", "Century Gothic", sans-serif;
  }
  .services text { fill: var(--card-ink); font-size: 19px; }
  .contact text { fill: var(--card-ink); font-size: 17px; }
  .holder-name { fill: var(--name-ink); font-size: 27px; }
  .holder-role { fill: var(--name-ink); font-size: 18px; }
</style>
</head>
<body>
<svg class="stage" viewBox="0 0 1200 896" xmlns="http://www.w3.org/2000/svg">
  <defs>
    <linearGradient id="silverFace" x1="0" y1="0" x2="1" y2="1">
      <stop offset="0" stop-color="var(--silver-light)"/>
      <stop offset="0.55" stop-color="var(--silver-mid)"/>
      <stop offset="1" stop-color="var(--silver-dark)"/>
    </linearGradient>
    <linearGradient id="tabTone" x1="0" y1="0" x2="1" y2="1">
      <stop offset="0" stop-color="var(--tab-light)"/>
      <stop offset="1" stop-color="var(--tab-dark)"/>
    </linearGradient>
    <clipPath id="frontClip"><rect x="0" y="0" width="540" height="310" rx="14"/></clipPath>
  </defs>

  <!-- Back of card: services -->
  <g class="card-back" transform="translate(40 150)">
    <rect width="540" height="310" rx="14" fill="var(--card-black)"/>
    <rect role="img" aria-label="Diagonal stripe accent" x="18" y="16" width="78" height="48" rx="10" fill="url(#tabTone)"/>
    <rect role="img" aria-label="Diagonal stripe accent" x="444" y="16" width="78" height="48" rx="10" fill="url(#tabTone)"/>
    <g class="services" text-anchor="middle">
      <text x="270" y="118">Hydroseeding</text>
      <text x="270" y="145">New lawn installations</text>
      <text x="270" y="172">Commercial Property Maintenance</text>
      <text x="270" y="199">Custom Outdoor Living Areas</text>
      <text x="270" y="226">Snow and Ice Management</text>
    </g>
  </g>

  <!-- Front of card: holder and contact -->
  <g class="card-front" transform="translate(620 436)">
    <g clip-path="url(#frontClip)">
      <rect width="540" height="310" fill="url(#silverFace)"/>
      <path d="M0 0 H230 L140 310 H0 Z" fill="#ffffff" opacity="0.18"/>
      <path class="contact-panel" d="M226 0 H540 V310 H226 Z" fill="var(--card-black)"/>
      <rect role="img" aria-label="Diagonal stripe accent" x="448" y="16" width="76" height="46" rx="10" fill="url(#tabTone)"/>
    </g>
    <text class="holder-name" x="212" y="160" text-anchor="end">Wesley R. Torvend</text>
    <text class="holder-role" x="212" y="184" text-anchor="end">Owner</text>
    <g class="contact" text-anchor="end">
      <text x="520" y="118">47 Birchell Lane</text>
      <text x="520" y="141">Palmer, MA 01082</text>
      <text x="520" y="172">(413) 555-0148</text>
      <text x="520" y="236" font-size="14">torvendlandscaping@quillmail.example</text>
    </g>
  </g>
</svg>
</body>
</html>
```